eBook book cover for erotic novel set in Singapore (yes really!)

Hello - here’s a bit of background on my book, along with some thoughts on the cover. I hope this helps; am happy to answer any questions and provide further example chapters if that would help you get a better idea of what it’s all about (some extracts are attached to this brief).

1. "Under Quiet Lanterns" - synopsis
“I'm curious—and tempted. Oh dear!” is Bea’s reply to an advert posted on the internet and she enters into a relationship unlike any other she has experienced before—one that stimulates, frustrates, consumes and ultimately, delights, her.

Owen a successful banker living in Singapore has placed an online invitation for “irregular intimacy” with a “sexy, well-dressed lover with stimulating kinks”. Bea’s feeling dulled by her demanding job and the undemanding social rituals of her life in Singapore: she’s attracted to Owen’s slightly jaded urbanity and quirky ways. He finds her plain-speaking exuberance a refreshing contrast to his own more conservative nature.

After a sparky, and at times, spiky, email exchange they meet at a rooftop bar in Singapore’s Chinatown. Over cocktails they agree the seven rules of their relationship (the first one—“No questions about work or personal lives”). Despite this formality, the sexual attraction between them is intense—as is the sex when they first manage to schedule it. Over subsequent weeks they craft a list of sexual experiences they intend to enjoy together. Once they’ve completed ‘The List’ (on an Excel spreadsheet) they’ll part. That’s the intention anyway.

As their relationship develops they both can’t help applying their controlling corporate selves to their secret life. Apart from the proposed experiences on the agreed list, each of them sometimes introduces new things to surprise the other. Under Quiet Lanterns is set mainly in Singapore—where the exotic sights, sounds and tastes provide a sensual backdrop to the increasingly intense affair.

The novel is about two people who believe they can manage their relationship in the same way they organise everything else in their lives—with closely calibrated calendar entries, tightly planned sexual liaisons and multiple lists. They relish the contrasts between their demanding jobs (the frequent travel, late night conference calls and always-on Quillphones) and indulging their imaginations with someone they trust. Bea begins to appreciate just what being “sex fit” entails. The sex scenes are explicit (“Sex where she did things she couldn’t tell her sisters about”) and driven in part by their competitive natures.

However, it gradually becomes clear that it is becoming harder for them to contain their relationship to just sex, no matter how delightful. They had both originally committed to a ‘no strings attached’ affair but they struggle with their growing feelings for each other. Owen initially drives the relationship but increasingly becomes out of his depth whilst Bea gains confidence. The novel ends with over half The List still to be completed—will they be able to keep to the rules, and more importantly, maintain the expected emotional distance they’ve both agreed to?

2. Cover thoughts
I’d like to avoid the typical cliched image of say, a silk tie and handcuffs, that one often sees on book covers of this genre. A reference to Singapore/Asia would be good of course (an orchid too obvious?), and naturally being an ebook, the cover needs to be simple and striking. I have a second book planned, and half written, and possibly a third. A design that thus lends itself to being adapted slightly so as to support a trilogy would be particularly useful.

3. Author's name
Gus Palmer

Thanks
Gus

Women 25-45

Serif
Decorative
Script

85cae6
3176b5

• A reference to Asia/Singapore
• A sense of the unknown, reference to Asia/Singapore, a hint of sex attraction, reference to corporate life.
• Just had a thought that a single stiletto shoe (on a carpet, wooden floorboards?) might be interesting.
• Be overly explicit sexually - have the usual cliche of a scantily clad woman for example

```html
<!DOCTYPE html>
<html lang="en">
<head>
<meta charset="utf-8">
<title>Under Quiet Lanterns — Gus Palmer</title>
<link rel="stylesheet" href="https://fonts.googleapis.com/css2?family=Playball&family=Noto+Sans+TC:wght@400&family=Open+Sans:wght@700&display=swap">
<style>
  :root {
    --paper: #ffffff;
    --cover-red: #e31b1b;
    --ink: #111111;
    --skin-light: #f6dccd;
    --skin-mid: #e9bfa8;
    --shoe-black: #1a1a1a;
    --fan-gold: #f6c64a;
    --fan-light: #fbdc7e;
  }
  html, body {
    margin: 0;
    padding: 0;
    overflow: hidden;
    background: var(--paper);
  }
  .cover {
    position: relative;
    width: 750px;
    height: 1200px;
    overflow: hidden;
    background: var(--paper);
  }
  .cover-photo {
    position: absolute;
    left: 70px;
    top: 0;
    width: 460px;
    height: 985px;
    background: linear-gradient(180deg, var(--skin-light) 0%, var(--skin-mid) 55%, var(--skin-light) 72%, var(--shoe-black) 82%, var(--shoe-black) 96%, var(--paper) 100%);
    opacity: 0.85;
  }
  .title-chinese {
    position: absolute;
    left: 38px;
    top: 600px;
    margin: 0;
    writing-mode: vertical-rl;
    font-family: "Noto Sans TC", sans-serif;
    font-weight: 400;
    font-size: 68px;
    line-height: 1;
    letter-spacing: 4px;
    color: var(--cover-red);
  }
  .title {
    position: absolute;
    left: 320px;
    top: 640px;
    width: 410px;
    margin: 0;
    text-align: center;
    font-family: "Playball", cursive;
    font-weight: 400;
    font-size: 88px;
    line-height: 108px;
    color: var(--cover-red);
  }
  .title span { display: block; }
  .author-band {
    position: absolute;
    left: 0;
    top: 1037px;
    width: 750px;
    height: 163px;
    background: var(--cover-red);
  }
  .author {
    position: absolute;
    left: 46px;
    top: 1132px;
    margin: 0;
    font-family: "Open Sans", sans-serif;
    font-weight: 700;
    font-size: 33px;
    line-height: 1;
    color: var(--ink);
  }
  .fan {
    position: absolute;
    left: 300px;
    top: 975px;
    width: 450px;
    height: 225px;
  }
</style>
</head>
<body>
  <main class="cover">
    <div class="cover-photo" role="img" aria-label="Photograph of a woman's bare legs, one foot slipping out of a black stiletto heel held in her hand"></div>

    <p class="title-chinese" lang="zh-Hant">靜靜的燈籠下</p>

    <h1 class="title">
      <span>Under</span>
      <span>Quiet</span>
      <span>Lanterns</span>
    </h1>

    <div class="author-band"></div>
    <p class="author">By Gus Palmer</p>

    <svg class="fan" viewBox="0 0 450 225" role="img" aria-label="Illustration of an open golden Chinese folding fan">
      <defs>
        <radialGradient id="fan-fill" cx="50%" cy="100%" r="100%">
          <stop offset="0%" stop-color="var(--fan-light)"/>
          <stop offset="100%" stop-color="var(--fan-gold)"/>
        </radialGradient>
      </defs>
      <path d="M0 225 A225 225 0 0 1 450 225 Z" fill="url(#fan-fill)"/>
    </svg>
  </main>
</body>
</html>
```